Refresh our Logo and Letterhead!

We would like to see designs with blue, green, teal etc. Our current logo and contact details for the letterhead is attached.
We're a small boutique firm based in Sydney, Australia. We're near the coast and not opposed to coastal images. We practice in property law and have primarily female practitioners, although we don't necessarily need the logo and letterhead to be too feminine. We would like to see designs with blue, green, teal etc. Our current logo and contact details for the letterhead is attached.
We're a small boutique firm based in Sydney, Australia. We're near the coast and not opposed to coastal images. We practice in property law and have primarily female practitioners, although we don't necessarily need the logo and letterhead to be too feminine.

Target Market(s)

Young professionals

Industry/Entity Type

Law Firm

Logo Text

Halvering Legal

Font styles to use
Serif
Sans Serif

Colors
34a7d8
00a990
85acd3
886aae

Requirements
Must have
• The letterhead must have the text in the "contact info" jpg uploaded with the brief.
Nice to have
• We'd like to see some simple, innovating, fresh ideas. A watermark or something interesting in the background would be good.

```html
<!DOCTYPE html>
<html lang="en">
<head>
<meta charset="utf-8">
<title>Halvering Legal – Stationery</title>
<link rel="stylesheet" href="https://fonts.googleapis.com/css2?family=Open+Sans:wght@300;400&family=Roboto:wght@400&display=swap">
<style>
  :root {
    --bg: #e4e5e8;
    --paper: #f7f7f7;
    --brand-blue: #2f6fb3;
    --brand-sky: #34a7d8;
    --ink: #4a4a4a;
    --ink-soft: #5c5c5c;
    --window-line: #cfd3d8;
  }
  * { box-sizing: border-box; margin: 0; padding: 0; }
  html, body { width: 1200px; height: 900px; overflow: hidden; }
  body {
    background: var(--bg);
    position: relative;
    font-family: "Open Sans", Arial, sans-serif;
  }

  /* Envelope */
  .envelope {
    position: absolute;
    left: 50px; top: 330px;
    width: 480px; height: 240px;
    background: var(--paper);
    box-shadow: 0 2px 6px rgba(0,0,0,.12);
  }
  .envelope .brand-name {
    position: absolute;
    left: 28px; top: 52px;
    font-size: 24px;
  }
  .envelope-window {
    position: absolute;
    left: 40px; top: 112px;
    width: 190px; height: 100px;
    border: 1px solid var(--window-line);
    background: #fbfbfb;
  }

  /* Shared brand name */
  .brand-name {
    font-family: "Open Sans", Arial, sans-serif;
    font-weight: 300;
    color: var(--brand-blue);
    display: flex;
    align-items: center;
    gap: 8px;
    white-space: nowrap;
    line-height: 1;
  }
  .brand-dot {
    width: 12px; height: 12px;
    border-radius: 50%;
    background: var(--brand-sky);
    flex: none;
  }

  /* Letterhead */
  .letterhead {
    position: absolute;
    left: 580px; top: 54px;
    width: 560px; height: 792px;
    background: var(--paper);
    box-shadow: 0 2px 8px rgba(0,0,0,.14);
    padding: 42px 40px 0 40px;
  }
  .letter-header {
    display: flex;
    justify-content: space-between;
    align-items: flex-start;
    gap: 16px;
    height: 128px;
  }
  .letterhead .brand-name {
    font-size: 26px;
    margin-top: 34px;
  }
  .contact-list {
    list-style: none;
    font-family: "Roboto", Arial, sans-serif;
    font-size: 10.5px;
    line-height: 14.6px;
    color: var(--ink);
    white-space: nowrap;
    flex: none;
  }
  .contact-list li { display: flex; align-items: center; gap: 4px; }
  .contact-list .icon { width: 9px; height: 10px; fill: var(--brand-blue); flex: none; }
  .contact-list .no-icon { padding-left: 2px; }

  .letter-body {
    font-size: 10.9px;
    line-height: 16px;
    color: var(--ink-soft);
    text-align: justify;
  }
  .letter-body p { margin-bottom: 16px; }
  .signature-area {
    width: 80px; height: 62px;
    margin: 4px 0 22px 0;
    background: #eeeeee;
  }
  .letter-footer {
    font-family: "Roboto", Arial, sans-serif;
    font-size: 10.3px;
    line-height: 14.6px;
    color: var(--ink);
    padding-left: 8px;
    width: 340px;
  }
  .letter-footer .firm { color: var(--brand-blue); }
  .letter-footer .label { color: var(--brand-blue); }
</style>
</head>
<body>

  <section class="envelope" aria-label="Envelope">
    <div class="brand-name"><span class="brand-dot"></span>Halvering Legal</div>
    <div class="envelope-window"></div>
  </section>

  <article class="letterhead" aria-label="Letterhead">
    <header class="letter-header">
      <div class="brand-name"><span class="brand-dot"></span>Halvering Legal</div>
      <ul class="contact-list">
        <li class="no-icon">P O Box 418, Avoca Beach NSW 2251</li>
        <li>
          <svg class="icon" viewBox="0 0 10 12" aria-hidden="true"><path d="M2 0h6a1 1 0 0 1 1 1v10a1 1 0 0 1-1 1H2a1 1 0 0 1-1-1V1a1 1 0 0 1 1-1zm.5 1.5v8h5v-8z"/></svg>
          0491 570 156
        </li>
        <li>
          <svg class="icon" viewBox="0 0 12 10" aria-hidden="true"><path d="M0 3c2-2 10-2 12 0l-1 2-2-1V2.8H3V4L1 5zM2.5 6L4 4.5h4L9.5 6v3.5h-7z"/></svg>
          02 4382 1190
        </li>
        <li>
          <svg class="icon" viewBox="0 0 12 10" aria-hidden="true"><path d="M3 0h6v3H3zM1 3.5h10v4H9V6H3v1.5H1zM3.5 6.5h5V10h-5z"/></svg>
          02 8155 2046
        </li>
        <li>
          <svg class="icon" viewBox="0 0 12 9" aria-hidden="true"><path d="M0 0h12v9H0zm1 1.2v.4l5 3.2 5-3.2v-.4z"/></svg>
          mara@halveringlegal.com.au
        </li>
        <li>
          <svg class="icon" viewBox="0 0 10 13" aria-hidden="true"><path d="M5 0a5 5 0 0 1 5 5c0 3-5 8-5 8S0 8 0 5a5 5 0 0 1 5-5zm0 3a2 2 0 1 0 0 4 2 2 0 0 0 0-4z"/></svg>
          12 Wattlebay Crescent Avoca Beach NSW 2251
        </li>
      </ul>
    </header>

    <div class="letter-body">
      <p>Dear customer,</p>
      <p>Lorem ipsum dolor sit amet, consectetur adipisicing elit, sed do eiusmod tempor incididunt ut labore et dolore magna aliqua. Ut enim ad minim veniam, quis nostrud exercitation ullamco laboris nisi ut aliquip ex ea commodo consequat. Duis aute irure dolor in reprehenderit in voluptate velit esse cillum dolore eu fugiat nulla pariatur. Excepteur sint occaecat cupidatat non proident, sunt in culpa qui officia deserunt mollit anim id est laborum.</p>
      <p>Lorem ipsum dolor sit amet, consectetur adipisicing elit, sed do eiusmod tempor incididunt ut labore et dolore magna aliqua. Ut enim ad minim veniam, quis nostrud exercitation ullamco laboris nisi ut aliquip ex ea commodo consequat. Duis aute irure dolor in reprehenderit in voluptate velit esse cillum dolore eu fugiat nulla pariatur. Excepteur sint occaecat cupidatat non proident, sunt in culpa qui officia deserunt mollit anim id est laborum.</p>
      <p>Lorem ipsum dolor sit amet, consectetur adipisicing elit, sed do eiusmod tempor incididunt ut labore et dolore magna aliqua. Ut enim ad minim veniam, quis nostrud exercitation ullamco laboris nisi ut aliquip ex ea commodo consequat. Duis aute irure dolor in reprehenderit in voluptate velit esse cillum dolore eu fugiat nulla pariatur. Excepteur sint occaecat cupidatat non proident, sunt in culpa qui officia deserunt mollit anim id est laborum.</p>
      <p>Lorem ipsum dolor sit amet, consectetur adipisicing elit, sed do eiusmod tempor incididunt ut labore et dolore magna aliqua. Ut enim ad minim veniam, quis nostrud exercitation ullamco laboris nisi ut aliquip ex ea commodo consequat. Duis aute irure dolor in reprehenderit.</p>
      <p>Yours Sincerely,</p>
      <div class="signature-area" role="img" aria-label="Handwritten signature of the sender"></div>
    </div>

    <footer class="letter-footer">
      <div class="firm">Halvering Legal Pty Ltd</div>
      <div><span class="label">ABN</span> : 51 824 753 116</div>
      <div>An incorporated legal practice under the Legal Profession Act 2004<br>as amended.</div>
      <div>Liability Limited by a scheme approved under Professional<br>Standards Legislation</div>
    </footer>
  </article>

</body>
</html>
```